Boutique personal training and fitness studio - banner ad design

We need a 'revolving' banner ad designed for our personal training and fitness studio. There are three separate offers (i.e. 3 pages to the advertisements)
Offer 1
PT Starter Pack
3 personal training sessions
$119
New clients only
Offer 2
Group fitness
2 weeks unlimited group fitness classes
$29
New clients only
Offer 3
Strength starter pack
2 weeks unlimited group fitness classes and 2 PT sessions
$89
New clients only
Please do not put the words "Offer 1, 2 or 3" in the ads - just the text following each offer.
Each advertisement should be sized to fit across around half of the webpage and be in landscape format.
Each advertisement should have a suitable picture (no cartoons) and should be complimentary to the existing website.
Each advertisement should also include the logo (attached)
www.corrabankliftworks.com.au
Training

```html
<!DOCTYPE html>
<html lang="en">
<head>
<meta charset="utf-8">
<title>Group Fitness Banners</title>
<link href="https://fonts.googleapis.com/css2?family=Oswald:wght@500;700&family=Tinos&display=swap" rel="stylesheet">
<style>
  :root {
    --page-bg: #e9e6e1;
    --panel-dark: #1d1d1d;
    --panel-stripe: #242424;
    --divider: #ffffff;
    --cream: #f4edd2;
    --silver-light: #ffffff;
    --silver-mid: #c9c9c9;
    --silver-dark: #7d7d7d;
    --logo-grey: #d6d6d6;
    --accent-blue: #1f3a9e;
    --accent-blue-light: #4a6fd6;
    --accent-red: #c8141b;
    --accent-red-light: #f04a4a;
  }
  * { margin: 0; padding: 0; box-sizing: border-box; }
  html, body {
    width: 1200px;
    height: 967px;
    overflow: hidden;
    background: var(--page-bg);
  }
  .canvas {
    position: relative;
    width: 1200px;
    height: 967px;
  }
  .banner {
    position: absolute;
    left: 227px;
    width: 780px;
    height: 388px;
    overflow: hidden;
    background:
      repeating-linear-gradient(45deg, var(--panel-dark) 0 3px, var(--panel-stripe) 3px 6px);
    --accent: var(--accent-blue);
    --accent-light: var(--accent-blue-light);
  }
  .banner--top { top: 100px; }
  .banner--bottom { top: 512px; }
  .banner--red {
    --accent: var(--accent-red);
    --accent-light: var(--accent-red-light);
  }
  .banner__photo {
    position: absolute;
    inset: 0;
    clip-path: polygon(0 0, 500px 0, 344px 100%, 0 100%);
  }
  .banner__photo--kettlebells {
    background: linear-gradient(160deg, #d9e4f0 0%, #5d6f86 30%, #2b3340 60%, #15191f 100%);
  }
  .banner__photo--cycling {
    background: linear-gradient(170deg, #f2f2f2 0%, #bfc3c6 35%, #8a6e6e 65%, #3d3536 100%);
  }
  .banner__divider {
    position: absolute;
    inset: 0;
    width: 780px;
    height: 388px;
  }
  .headline {
    position: absolute;
    right: 19px;
    font-family: "Oswald", sans-serif;
    font-weight: 700;
    font-size: 82px;
    line-height: 1;
    text-transform: uppercase;
    background: linear-gradient(180deg, var(--silver-light) 0%, var(--silver-mid) 45%, var(--silver-dark) 55%, var(--silver-light) 100%);
    -webkit-background-clip: text;
    background-clip: text;
    color: transparent;
  }
  .headline--first { top: 25px; }
  .headline--second { top: 102px; }
  .offer-line {
    position: absolute;
    right: 19px;
    font-family: "Oswald", sans-serif;
    font-weight: 700;
    font-size: 30px;
    line-height: 1;
    color: var(--cream);
    text-transform: uppercase;
  }
  .offer-line--first { top: 198px; }
  .offer-line--second { top: 227px; }
  .ribbon {
    position: absolute;
    left: 479px;
    top: 293px;
    width: 301px;
    height: 47px;
    background: linear-gradient(180deg, var(--accent-light) -60%, var(--accent) 60%);
    clip-path: polygon(0 0, 100% 0, 100% 100%, 14px 100%);
    display: flex;
    align-items: center;
    justify-content: center;
    padding-left: 14px;
    font-family: "Tinos", serif;
    font-size: 23px;
    color: #ffffff;
    text-transform: uppercase;
  }
  .price {
    position: absolute;
    left: 327px;
    top: 257px;
    width: 106px;
    height: 106px;
    border-radius: 50%;
    border: 4px solid #ffffff;
    background: radial-gradient(circle at 40% 30%, var(--accent-light) 0%, var(--accent) 65%);
    display: flex;
    align-items: center;
    justify-content: center;
    font-family: "Oswald", sans-serif;
    font-weight: 500;
    font-size: 44px;
    color: #ffffff;
  }
  .brand {
    position: absolute;
    font-family: "Oswald", sans-serif;
    font-weight: 700;
    font-size: 16px;
    line-height: 1.1;
    color: var(--logo-grey);
    text-transform: uppercase;
    text-align: center;
    letter-spacing: 1px;
  }
  .brand--bottom-left { left: 196px; top: 332px; }
  .brand--top { left: 328px; top: 18px; color: #6a6a6a; }
</style>
</head>
<body>
<main class="canvas">

  <section class="banner banner--top" aria-label="Group fitness offer, blue">
    <div class="banner__photo banner__photo--kettlebells" role="img" aria-label="Photo of a group doing push-ups on kettlebells in a gym"></div>
    <svg class="banner__divider" viewBox="0 0 780 388" aria-hidden="true">
      <line x1="503" y1="0" x2="347" y2="388" stroke="var(--divider)" stroke-width="5"/>
    </svg>
    <h2 class="headline headline--first">Group</h2>
    <h2 class="headline headline--second">Fitness</h2>
    <p class="offer-line offer-line--first">2 Weeks Unlimited</p>
    <p class="offer-line offer-line--second">Group Fitness Classes</p>
    <p class="ribbon">New Clients Only!</p>
    <p class="price">$29</p>
    <p class="brand brand--bottom-left">Corrabank<br>Liftworks</p>
  </section>

  <section class="banner banner--bottom banner--red" aria-label="Group fitness offer, red">
    <div class="banner__photo banner__photo--cycling" role="img" aria-label="Photo of women riding spin bikes in a bright studio"></div>
    <svg class="banner__divider" viewBox="0 0 780 388" aria-hidden="true">
      <line x1="503" y1="0" x2="347" y2="388" stroke="var(--divider)" stroke-width="5"/>
    </svg>
    <h2 class="headline headline--first">Group</h2>
    <h2 class="headline headline--second">Fitness</h2>
    <p class="offer-line offer-line--first">2 Weeks Unlimited</p>
    <p class="offer-line offer-line--second">Group Fitness Classes</p>
    <p class="ribbon">New Clients Only!</p>
    <p class="price">$29</p>
    <p class="brand brand--top">Corrabank<br>Liftworks</p>
  </section>

</main>
</body>
</html>
```